Velmora Partners - website for real estate investment company

Create a bold, modern website that reflects Velmora’s success, professionalism, and credibility.
The design must stand out while maintaining a polished, corporate tone. (bold, but understated)
The client just created a new logo, and the website design must be in sync with the logo design. Information about the logo colors, fonts, and message are in the attached design brief.
Updates

Target Market(s)

b2b: banks, brokers, institutional partners, vendors, and property sellers.

Industry/Entity Type

real estate investment company

Number of Pages Required

1 page

Font styles to use
Sans Serif

Colors

Designer to choose colors to be used in the design.

Requirements
Must have
• 1. homepage design (psd) 2. a top banner image (psd) for a default inner page
Nice to have
• please see attached design brief
Should not have

```html
<!DOCTYPE html>
<html lang="en">
<head>
<meta charset="utf-8">
<title>Velmora Partners</title>
<link href="https://fonts.googleapis.com/css2?family=Montserrat:wght@400;500;600;700;800&display=swap" rel="stylesheet">
<style>
:root{
  --red:#d71f26;
  --ink:#1d1d1f;
  --text:#555a60;
  --white:#ffffff;
  --light:#f3f3f3;
  --line:#d9d9d9;
  --navy:#1f2a3a;
  --footer:#1a1a1a;
  --footer-bar:#101010;
}
*{box-sizing:border-box;margin:0;padding:0}
html,body{width:1200px;height:4516px;overflow:hidden}
body{font-family:"Montserrat",Arial,sans-serif;color:var(--ink);background:var(--white);position:relative}
section,header,footer{position:relative;width:1200px}
.abs{position:absolute}
.btn{display:inline-block;background:var(--red);color:var(--white);font-size:13px;font-weight:600;letter-spacing:.5px;padding:14px 26px;text-transform:uppercase}
.btn-outline{background:var(--white);color:var(--ink);border:1px solid var(--ink)}
.btn-outline-light{background:transparent;border:1px solid var(--white)}
.title{font-size:34px;font-weight:700;letter-spacing:1px;text-transform:uppercase;display:inline-flex;align-items:flex-start;gap:8px}
.title svg{width:16px;height:14px;margin-top:2px}
.body-text{font-size:15px;line-height:1.65;color:var(--text)}

/* Hero */
.hero{height:720px;background:linear-gradient(180deg,#2b3d55 0%,#1f2a38 45%,#3a3026 100%)}
.hero-photo{position:absolute;inset:0;background:linear-gradient(160deg,rgba(40,70,110,.9),rgba(20,25,35,.85) 55%,rgba(110,80,50,.8))}
.nav{position:absolute;top:0;left:0;width:1200px;height:100px;display:flex;align-items:center;padding:0 112px}
.brand{font-size:34px;font-weight:800;color:var(--white);letter-spacing:1px}
.nav-links{margin-left:auto;display:flex;gap:34px;align-items:center;font-size:14px;font-weight:500;color:var(--white)}
.nav-links .active{border-bottom:2px solid var(--white);padding-bottom:4px}
.hero h1{position:absolute;top:196px;width:100%;text-align:center;color:var(--white);font-size:48px;font-weight:800;letter-spacing:3px;text-transform:uppercase}
.hero-lead{position:absolute;top:276px;left:260px;width:680px;text-align:center;color:#e8e8e8;font-size:17px;line-height:1.6}
.hero .btn{position:absolute;top:400px;left:520px;width:160px;text-align:center}
.stat{position:absolute;top:520px;height:120px;background:var(--white);display:flex;flex-direction:column;align-items:center;justify-content:center;text-align:center}
.stat strong{font-size:30px;font-weight:800}
.stat span{font-size:12px;color:var(--text);margin-top:6px;line-height:1.4}

/* About */
.about{height:480px}
.about .title{position:absolute;left:112px;top:100px}
.about .body-text{position:absolute;left:112px;top:170px;width:400px}
.about .btn{position:absolute;left:112px;top:350px}
.about-photo{position:absolute;left:600px;top:80px;width:472px;height:340px;background:linear-gradient(135deg,#c9d3dc,#8f9ea8 60%,#5d6b70)}
.corner{position:absolute;width:0;height:0;border-style:solid}

/* Sectors */
.sectors{height:840px;background:linear-gradient(180deg,#3e5266,#26313d 60%,#3a4655)}
.panel{position:absolute;background:var(--white)}
.sectors .panel{left:160px;top:92px;width:872px;height:640px}
.sectors .title{position:absolute;top:50px;width:100%;justify-content:center}
.sector-img{position:absolute;width:336px;height:240px}
.sector-name{font-size:15px;font-weight:700;text-transform:uppercase;display:flex;gap:8px;align-items:center}
.sector-text{position:absolute;width:360px}
.sector-text .body-text{font-size:14px;margin-top:10px}

/* Apart */
.apart{height:720px;background:var(--white)}
.apart .title{position:absolute;top:44px;width:100%;justify-content:center}
.card{position:absolute;top:120px;width:280px;height:440px;background:var(--white);box-shadow:0 6px 24px rgba(0,0,0,.12);text-align:center;padding:40px 28px}
.card.featured{background:var(--red);color:var(--white)}
.card .icon{width:100px;height:100px;margin:0 auto 28px;background:var(--navy);display:flex;align-items:center;justify-content:center}
.card.featured .icon{background:var(--white)}
.card h3{font-size:19px;font-weight:700;line-height:1.35}
.card p{font-size:14px;line-height:1.6;color:var(--text);margin-top:16px}
.card.featured p{color:var(--white)}
.apart .btn{position:absolute;top:592px;left:460px;width:280px;text-align:center}

/* Partner */
.partner{height:400px;background:linear-gradient(135deg,#4b5866,#2d3641 50%,#6f7880)}
.partner .panel{left:180px;top:60px;width:840px;height:280px;background:rgba(255,255,255,.92);text-align:center;padding-top:50px}
.partner p{font-size:17px;line-height:1.6;color:var(--text);width:620px;margin:18px auto 0}
.partner .actions{margin-top:26px;display:flex;gap:20px;justify-content:center}

/* Contact */
.contact{height:840px}
.contact .title{position:absolute;top:156px;width:100%;justify-content:center}
.contact .lead{position:absolute;top:230px;left:180px;width:840px;text-align:center;font-size:18px;line-height:1.6;color:var(--text)}
.contact-box{position:absolute;left:200px;top:460px;width:360px;height:300px;background:var(--red);color:var(--white);padding:36px 32px}
.contact-box h4{font-size:17px;font-weight:700;text-transform:uppercase;display:flex;gap:8px;align-items:center}
.contact-box ul{list-style:none;margin-top:20px}
.contact-box li{display:flex;gap:12px;align-items:center;font-size:14px;margin-bottom:14px}
.contact-box .btn{background:var(--white);color:var(--ink);padding:12px 22px;margin-top:16px}
.form{position:absolute;left:560px;top:460px;width:440px;height:340px;background:var(--light);padding:30px 40px}
.field{height:46px;background:var(--white);border:1px solid var(--line);font-size:12px;color:#999;padding:15px 16px;text-transform:uppercase;margin-bottom:18px}
.field.tall{height:120px}

/* Footer */
.footer{height:472px;background:var(--footer);color:var(--white)}
.footer .brand{position:absolute;left:112px;top:90px;font-size:42px}
.footer .tag{position:absolute;left:112px;top:200px;font-size:15px;line-height:1.5}
.footer .btn{position:absolute;left:112px;top:270px;background:transparent;border:1px solid var(--white);padding:12px 24px}
.footer h5{font-size:19px;font-weight:700;text-transform:uppercase;display:flex;gap:8px;align-items:center}
.col{position:absolute;top:110px}
.col ul{list-style:none;margin-top:24px}
.col li{font-size:14px;text-transform:uppercase;margin-bottom:14px}
.col.contact-col li{text-transform:none;display:flex;gap:12px;align-items:center}
.copyright{height:44px;background:var(--footer-bar);color:#bbb;font-size:13px;text-align:center;line-height:44px}
</style>
</head>
<body>

<header class="hero">
  <div class="hero-photo" role="img" aria-label="Modern apartment building at dusk"></div>
  <nav class="nav">
    <div class="brand">VELMORA</div>
    <div class="nav-links">
      <span class="active">HOME</span><span>OUR STORY</span><span>INVESTMENT STRATEGY</span><span>OUR PORTFOLIO</span>
      <span class="btn">Contact Us</span>
    </div>
  </nav>
  <h1>Experience – Strategy – Vision</h1>
  <p class="hero-lead">Velmora Partners is a vertically integrated real estate investment firm with a proven four-decade track record. We acquire, reposition, and operate high-performing assets across multiple sectors — always with a focus on exceptional, risk-adjusted returns.</p>
  <span class="btn">Get Started</span>
  <div class="stat" style="left:272px;width:160px"><strong>1989</strong><span>Founded</span></div>
  <div class="stat" style="left:512px;width:176px"><strong>23,000+</strong><span>Multifamily &amp;<br>Healthcare units</span></div>
  <div class="stat" style="left:768px;width:176px"><strong>$300M+</strong><span>Invested in<br>renovations</span></div>
</header>

<section class="about">
  <h2 class="title">About Velmora<svg viewBox="0 0 16 14"><path d="M0 0H16L0 14Z" fill="#d71f26"/></svg></h2>
  <p class="body-text">For more than 40 years, Velmora Partners has built a reputation for disciplined acquisitions, strategic repositioning, and operational excellence. We bring an institutional approach with an entrepreneurial edge, delivering value through every market cycle: strategic repositioning, and operational excellence.</p>
  <span class="btn">Learn Our Story</span>
  <div class="about-photo" role="img" aria-label="Business partners reviewing a property site plan"></div>
  <div class="corner" style="left:1032px;top:380px;border-width:0 0 40px 40px;border-color:transparent transparent var(--red) transparent"></div>
</section>

<section class="sectors" role="img" aria-label="Office towers in the background">
  <div class="panel">
    <h2 class="title">Our Sectors<svg viewBox="0 0 16 14"><path d="M0 0H16L0 14Z" fill="#d71f26"/></svg></h2>
    <div class="sector-img" style="left:104px;top:128px;background:linear-gradient(160deg,#6b4a36,#a77a58 50%,#3a3026)" role="img" aria-label="Senior care residence at dusk"></div>
    <div class="sector-text" style="left:460px;top:160px">
      <div class="sector-name">Skilled Nursing &amp; Healthcare <span style="color:var(--red)">→</span></div>
      <p class="body-text">With deep operational expertise in healthcare, we optimize performance while maintaining the highest standards of care and compliance, ensuring strong returns and resident well-being.</p>
    </div>
    <div class="sector-text" style="left:104px;top:408px">
      <div class="sector-name">Multifamily Communities <span style="color:var(--red)">→</span></div>
      <p class="body-text">From urban high-rises to suburban garden-style apartments, we enhance property performance and resident satisfaction through targeted renovations, operational efficiencies, and strategic repositioning.</p>
    </div>
    <div class="sector-img" style="left:460px;top:320px;width:380px;height:248px;background:linear-gradient(160deg,#8fb0cf,#a68a6a 55%,#4f6b3a)" role="img" aria-label="Apartment community with landscaped gardens"></div>
    <div class="corner" style="left:460px;top:528px;border-width:40px 0 0 40px;border-color:transparent transparent transparent var(--red)"></div>
  </div>
</section>

<section class="apart">
  <h2 class="title">What Sets Us Apart<svg viewBox="0 0 16 14"><path d="M0 0H16L0 14Z" fill="#d71f26"/></svg></h2>
  <div class="card featured" style="left:112px">
    <div class="icon"><svg width="52" height="52" viewBox="0 0 52 52" fill="none" stroke="#1f2a3a" stroke-width="3"><circle cx="26" cy="26" r="9"/><circle cx="26" cy="26" r="18" stroke-dasharray="6 5"/></svg></div>
    <h3>Vertically Integrated Operations Vertically</h3>
    <p>We manage the entire investment lifecycle in-house, from acquisition and repositioning to ongoing operations.</p>
  </div>
  <div class="card" style="left:460px">
    <div class="icon"><svg width="52" height="52" viewBox="0 0 52 52" fill="none" stroke="#fff" stroke-width="3"><path d="M8 44V8M8 44H46"/><path d="M14 36L24 24L32 30L44 14"/></svg></div>
    <h3>Cycle-Tested Investment Strategies</h3>
    <p>Decades of experience navigating market cycles allow us to identify and execute on opportunities others might miss.</p>
  </div>
  <div class="card" style="left:808px">
    <div class="icon"><svg width="52" height="52" viewBox="0 0 52 52" fill="none" stroke="#fff" stroke-width="3"><rect x="8" y="6" width="36" height="40"/><path d="M16 36V28M26 36V20M36 36V14"/></svg></div>
    <h3>In-House Asset Management</h3>
    <p>Our dedicated asset management team ensures every property meets performance and quality benchmarks.</p>
  </div>
  <span class="btn">Discover Our Strategy</span>
</section>

<section class="partner" role="img" aria-label="Glass office buildings at sunset">
  <div class="panel">
    <h2 class="title">Partner with Velmora Partners<svg viewBox="0 0 16 14"><path d="M0 0H16L0 14Z" fill="#d71f26"/></svg></h2>
    <p>Join forces with an investment firm that delivers performance, stability, and lasting value — through every market cycle.</p>
    <div class="actions"><span class="btn">Contact Us</span><span class="btn btn-outline">Career Opportunities</span></div>
  </div>
</section>

<section class="contact">
  <h2 class="title">Get in Touch<svg viewBox="0 0 16 14"><path d="M0 0H16L0 14Z" fill="#d71f26"/></svg></h2>
  <p class="lead">Whether you're an investor, property owner, broker, or industry partner, we'd like to hear from you. Our team is ready to discuss opportunities, answer questions, and explore ways we can work together.</p>
  <div class="contact-box">
    <h4>Contact Details <span>→</span></h4>
    <ul>
      <li><svg width="14" height="18" viewBox="0 0 14 18"><path d="M7 0C3 0 0 3 0 7c0 5 7 11 7 11s7-6 7-11c0-4-3-7-7-7z" fill="#fff"/><circle cx="7" cy="7" r="2.5" fill="#d71f26"/></svg>420 Harbor Ave, Lakeview, NJ 07010</li>
      <li><svg width="16" height="16" viewBox="0 0 16 16"><path d="M3 1l3 3-2 2c1 2 3 4 5 5l2-2 3 3-2 3C6 15 1 10 1 3z" fill="#fff"/></svg>(555) 204-7781</li>
      <li><svg width="16" height="12" viewBox="0 0 16 12"><rect width="16" height="12" fill="#fff"/><path d="M0 0l8 6 8-6" stroke="#d71f26" fill="none"/></svg>info@velmora.com</li>
    </ul>
    <h4 style="margin-top:22px">Career Inquiries <span>→</span></h4>
    <span class="btn">Email Us</span>
  </div>
  <div class="form">
    <div class="field">Enter Name</div>
    <div class="field">Enter Email</div>
    <div class="field tall">Message</div>
    <span class="btn">Submit</span>
  </div>
</section>

<footer class="footer">
  <div class="brand">VELMORA</div>
  <p class="tag">Trusted Real Estate Investment<br>Since 1989</p>
  <span class="btn">Email Us</span>
  <div class="col" style="left:520px">
    <h5>Quick Links<svg width="14" height="12" viewBox="0 0 16 14"><path d="M0 0H16L0 14Z" fill="#d71f26"/></svg></h5>
    <ul><li>Home</li><li>Our Story</li><li>Investment Strategy</li><li>What Sets Us Apart</li><li>Our Portfolio</li><li>Contact</li></ul>
  </div>
  <div class="col contact-col" style="left:844px">
    <h5>Contact Details<svg width="14" height="12" viewBox="0 0 16 14"><path d="M0 0H16L0 14Z" fill="#d71f26"/></svg></h5>
    <ul>
      <li><svg width="14" height="18" viewBox="0 0 14 18"><path d="M7 0C3 0 0 3 0 7c0 5 7 11 7 11s7-6 7-11c0-4-3-7-7-7z" fill="#d71f26"/></svg>420 Harbor Ave, Lakeview, NJ 07010</li>
      <li><svg width="16" height="16" viewBox="0 0 16 16"><path d="M3 1l3 3-2 2c1 2 3 4 5 5l2-2 3 3-2 3C6 15 1 10 1 3z" fill="#d71f26"/></svg>(555) 204-7781</li>
      <li><svg width="16" height="12" viewBox="0 0 16 12"><rect width="16" height="12" fill="#d71f26"/><path d="M0 0l8 6 8-6" stroke="#1a1a1a" fill="none"/></svg>info@velmora.com</li>
    </ul>
  </div>
</footer>
<div class="copyright">© 2025 Velmora Partners. All Rights Reserved.</div>

</body>
</html>
```